Midnight Lantern Diva

We have started working on a website for our short film. The goals of this website are:
• Attract talent, financiers + distributors to the feature film.
• Start e-commerce business to generate buzz for the film.

Who is our target audience?
• Kung Fu fans.
• Guitar players.
• Women filmmakers.
• Chinese film fans.

Information we want on this website.
Web 1.0 Components
• Media - trailer and stills

We are looking to include the following pages:
1. Home page
2. About
3. Photos
4. Cast & Crew
5. News
6. Media (reviews)
7. Store
8. Contact

Web 2.0 Components
• Mailing list sign-up
• Blog - with comments section
• Like / Add buttons - to all social networks
• Feeds - from social media
• Links - social media
• Widgets - that anyone can put on their sites

Attached is a mock up of the landing page (possible T-shirt) we are developing plus photos we would like on the website.

Thank you.
Updates

Reason: I am at a film market in meetings for my film project. Next week will be used for script rewrites. After that I will choose a design.

Hello Folks,

I have added my company logo to my brief. My answer is yes - I would like that added to the website.
Thanks!
M-

Reason: I have added more photos and included two (in front of a white screen) that can easily be photoshopped into a great landing page. M-

I have added more photos. Also I have two photos taken in front of a white screen that can easily be photo-shopped into a cool landing page. I have also gotten rid of the "crowd" photo in my mock up of the design I am looking for. 

I've extended the deadline by 2 days.

M-

Target Market(s)

• Kung Fu fans.
• Guitar players.
• Women filmmakers.
• Chinese film fans.

Industry/Entity Type

E-Commerce

Colors
ec2027

Requirements
Must have
• Trailer, movie stills, links to social media.
Nice to have
• All of the above

```html
<!DOCTYPE html>
<html lang="en">
<head>
<meta charset="utf-8">
<title>Contact – Midnight Lantern Diva</title>
<link href="https://fonts.googleapis.com/css2?family=Lato:wght@300;400;700;900&display=swap" rel="stylesheet">
<style>
  :root{
    --red:#ec2027;
    --red-soft:#e8393c;
    --ink:#1a1a1a;
    --text:#333333;
    --panel:#333333;
    --panel-line:#5a5a5a;
    --white:#ffffff;
    --fan-text:#ffd0d1;
  }
  *{box-sizing:border-box;margin:0;padding:0}
  html,body{width:720px;height:1200px;overflow:hidden;background:var(--white)}
  body{position:relative;font-family:'Lato',sans-serif;color:var(--text)}

  .main-nav{position:absolute;top:24px;left:0;width:720px;height:16px}
  .main-nav a{position:absolute;top:0;font-size:11px;color:#444;text-decoration:none;letter-spacing:.2px}
  .main-nav a.is-current{color:var(--red);font-weight:700}

  .hero-banner{position:absolute;left:17px;top:48px;width:686px;height:189px;
    background:radial-gradient(ellipse at 55% 60%,#b0122a 0%,#7a0c1c 45%,#3a050c 100%);
    display:flex;align-items:center;padding-left:36px}
  .hero-banner .hero-title{font-weight:900;font-size:38px;color:var(--white);letter-spacing:.5px}

  .contact-list{position:absolute;left:42px;top:264px;width:332px}
  .contact-block{height:197px}
  .contact-block h2{font-size:14.5px;font-weight:700;color:var(--ink);padding-bottom:6px;border-bottom:1.5px solid var(--red-soft);margin-bottom:9px}
  .contact-block p{font-size:8.5px;line-height:13.1px;color:#333;white-space:nowrap;letter-spacing:-.05px}
  .contact-links{margin-top:12px;font-size:9px;font-weight:700;line-height:13px}
  .contact-links a{display:block;color:var(--red);text-decoration:none}

  .signup{position:absolute;left:403px;top:268px;width:155px;height:23px;border:1px solid #c8c8c8;border-radius:3px;font-size:6.8px;font-weight:700;color:#555;padding:7px 0 0 4px}
  .social-links{position:absolute;left:566px;top:264px;display:flex;gap:6px}
  .social-links span{display:flex;align-items:center;justify-content:center;width:33px;height:30px;background:var(--red);border-radius:3px;color:var(--white);font-size:6px;font-weight:700}

  .tweet-panel{position:absolute;left:403px;top:313px;width:270px;height:324px;background:var(--panel);border-radius:6px;color:var(--white)}
  .tweet-panel .panel-title{position:absolute;left:18px;top:15px;font-size:13px;font-weight:400}
  .follow-btn{position:absolute;left:125px;top:11px;width:128px;height:21px;background:#e6e6e6;border-radius:3px;font-size:6.6px;font-weight:700;color:#444;display:flex;align-items:center;justify-content:center;gap:4px}
  .follow-btn i{width:8px;height:8px;background:var(--red);border-radius:50%}
  .panel-rule{position:absolute;left:18px;width:234px;height:1px;background:var(--panel-line)}
  .tweet{position:absolute;left:18px;width:234px;height:62px}
  .tweet-avatar{position:absolute;left:0;top:0;width:57px;height:57px;background:linear-gradient(135deg,#6a1230,#b0325a 60%,#3b0a1c)}
  .tweet-body{position:absolute;left:63px;top:2px;font-size:10.5px;line-height:13.5px;font-weight:400}
  .tweet-body strong{font-weight:700;font-size:10px}
  .tweet-body .tag{color:var(--red-soft)}
  .tweet-body .expand{font-size:7.5px;color:#ddd}
  .tweet-time{position:absolute;right:7px;top:4px;font-size:8px;color:#ccc}
  .tweet-field{position:absolute;left:18px;top:287px;width:234px;height:20px;background:#c9c9c9;border-radius:3px;font-size:6.8px;font-weight:700;color:#555;padding:6px 0 0 4px}

  .fan-panel{position:absolute;left:403px;top:659px;width:270px;height:314px;background:var(--red);border-radius:6px;color:var(--white)}
  .fan-panel h3{position:absolute;left:20px;top:20px;font-size:12.5px;font-weight:700}
  .fan-panel .panel-rule{top:42px;left:20px;width:226px;background:#f38a8d}
  .fan-panel p{position:absolute;left:20px;top:61px;font-size:10.5px;font-weight:300;line-height:14px;color:var(--fan-text)}
  .studio-card{position:absolute;left:18px;top:112px;width:231px;height:182px;background:var(--white);display:flex;align-items:center;justify-content:center;gap:8px}
  .studio-card i{width:18px;height:18px;border-radius:50%;background:var(--red)}
  .studio-card span{font-size:17px;font-weight:700;color:var(--red)}

  .site-footer{position:absolute;left:17px;top:1144px;width:686px;border-top:1px solid #e88;padding:14px 0 0 25px;font-size:6px;color:#222}
</style>
</head>
<body>
  <nav class="main-nav">
    <a href="#" style="left:42px">HOME</a>
    <a href="#" style="left:113px">ABOUT</a>
    <a href="#" style="left:190px">NEWS</a>
    <a href="#" style="left:272px">MEDIA</a>
    <a href="#" style="left:347px">PHOTOS</a>
    <a href="#" style="left:431px">CAST &amp; CREW</a>
    <a href="#" style="left:540px">STORE</a>
    <a href="#" class="is-current" style="left:614px">CONTACT</a>
  </nav>

  <header class="hero-banner" role="img" aria-label="Red starry banner with the film title and the lead actress in a flying kick">
    <span class="hero-title">Midnight Lantern Diva</span>
  </header>

  <main class="contact-list">
    <section class="contact-block">
      <h2>Contact Us Distribution</h2>
      <p>Text for home page Otatiis minctur? Quiae cum fuga. Ovid erument que alibusdae.<br>Ut odi voluptatius, idundae. Et aliqui con nim id quas moditiam, odia delenem fac-<br>cat iur, aped moluptate nis di cuptis nist reptas evelici toria vollent expelen dignis<br>as quae corrorpor aut eos eum inulpa dolorehenit por si doluptur? Optatus mi,<br>que sunt, que ne perum apiet vendis autest, sumenis accus dicti re nihitas eum,<br>officipici iur, ut pratum quoste landenis experovit dita ipsam fuga. Rae et lantint<br>andanti ducimusandes siti quae venducimus.</p>
      <div class="contact-links"><a href="#">Email</a><a href="#">Telephone</a></div>
    </section>
    <section class="contact-block">
      <h2>Contact Us Advertise</h2>
      <p>Text for home page Otatiis minctur? Quiae cum fuga. Ovid erument que alibusdae.<br>Ut odi voluptatius, idundae. Et aliqui con nim id quas moditiam, odia delenem fac-<br>cat iur, aped moluptate nis di cuptis nist reptas evelici toria vollent expelen dignis<br>as quae corrorpor aut eos eum inulpa dolorehenit por si doluptur? Optatus mi,<br>que sunt, que ne perum apiet vendis autest, sumenis accus dicti re nihitas eum,<br>officipici iur, ut pratum quoste landenis experovit dita ipsam fuga. Rae et lantint<br>andanti ducimusandes siti quae venducimus.</p>
      <div class="contact-links"><a href="#">Email</a><a href="#">Telephone</a></div>
    </section>
    <section class="contact-block">
      <h2>Contact Us Press Releases</h2>
      <p>Text for home page Otatiis minctur? Quiae cum fuga. Ovid erument que alibusdae.<br>Ut odi voluptatius, idundae. Et aliqui con nim id quas moditiam, odia delenem fac-<br>cat iur, aped moluptate nis di cuptis nist reptas evelici toria vollent expelen dignis<br>as quae corrorpor aut eos eum inulpa dolorehenit por si doluptur? Optatus mi,<br>que sunt, que ne perum apiet vendis autest, sumenis accus dicti re nihitas eum,<br>officipici iur, ut pratum quoste landenis experovit dita ipsam fuga. Rae et lantint<br>andanti ducimusandes siti quae venducimus.</p>
      <div class="contact-links"><a href="#">Email</a><a href="#">Telephone</a></div>
    </section>
    <section class="contact-block">
      <h2>Contact Us Press Releases</h2>
      <p>Text for home page Otatiis minctur? Quiae cum fuga. Ovid erument que alibusdae.<br>Ut odi voluptatius, idundae. Et aliqui con nim id quas moditiam, odia delenem fac-<br>cat iur, aped moluptate nis di cuptis nist reptas evelici toria vollent expelen dignis<br>as quae corrorpor aut eos eum inulpa dolorehenit por si doluptur? Optatus mi,<br>que sunt, que ne perum apiet vendis autest, sumenis accus dicti re nihitas eum,<br>officipici iur, ut pratum quoste landenis experovit dita ipsam fuga. Rae et lantint<br>andanti ducimusandes siti quae venducimus.</p>
      <div class="contact-links"><a href="#">Email</a><a href="#">Telephone</a></div>
    </section>
  </main>

  <div class="signup">Yes, send me news to my email address</div>
  <div class="social-links">
    <span>Chirpline</span><span>Facepage</span><span>Feedwire</span>
  </div>

  <aside class="tweet-panel">
    <div class="panel-title">Tweets</div>
    <div class="follow-btn"><i></i>Follow @MidnightLanternDiva</div>
    <div class="panel-rule" style="top:37px"></div>

    <div class="tweet" style="top:56px">
      <div class="tweet-avatar" role="img" aria-label="Profile photo of the lead actress"></div>
      <div class="tweet-body"><strong>Midnight Lantern Diva</strong><br>Chirpline Feed News Goes here<br><span class="tag"># ChirplineFeedTag</span><br><span class="expand">Expand</span></div>
      <span class="tweet-time">2min</span>
    </div>
    <div class="panel-rule" style="top:124px"></div>
    <div class="tweet" style="top:128px">
      <div class="tweet-avatar" role="img" aria-label="Profile photo of the lead actress"></div>
      <div class="tweet-body"><strong>Midnight Lantern Diva</strong><br>Chirpline Feed News Goes here<br><span class="tag"># ChirplineFeedTag</span><br><span class="expand">Expand</span></div>
      <span class="tweet-time">2min</span>
    </div>
    <div class="panel-rule" style="top:196px"></div>
    <div class="tweet" style="top:200px">
      <div class="tweet-avatar" role="img" aria-label="Profile photo of the lead actress"></div>
      <div class="tweet-body"><strong>Midnight Lantern Diva</strong><br>Chirpline Feed News Goes here<br><span class="tag"># ChirplineFeedTag</span><br><span class="expand">Expand</span></div>
      <span class="tweet-time">2min</span>
    </div>
    <div class="panel-rule" style="top:268px"></div>
    <div class="tweet-field">Tweet to @MidnightLanternDiva</div>
  </aside>

  <aside class="fan-panel">
    <h3>Fan Page</h3>
    <div class="panel-rule"></div>
    <p>Want to know all the inside gossip?<br>Then follow our fan page on Facepage.</p>
    <div class="studio-card"><i></i><span>Silver Tide Pictures</span></div>
  </aside>

  <footer class="site-footer">Midnight Lantern Diva is a Silver Tide Pictures production © 2014</footer>
</body>
</html>
```